"TR wanderer" Périple Transportation Company with vehicles not exceeding 9 seats. shuttle kil

Need a design full of freshness to make a trip relaxing drive, comfortable, safe, ideal for a trip with confidence. Punctuality. A positive visual impact, enter information about the company, a logo that stands out from other competitors but remains both simple and enjoyable ... Trust, punctuality, relaxing, stress. Generosity in the passenger transport service, mainly for airport shuttles between Paris and Normandy, but also any kind of distance, France and Europe, as long as there is a road we can go

Target Market(s)

Airport Shuttle Service and all distances for the companies and individuals

Industry/Entity Type

Transfer

Contact Information for Business Card

Société : TR Périple, Luc Barnier
Adresse : Rue Paul Dantier, Bâtiment KRP, 76420 Bellerive, 0672418053, l.barnier@trperiple.fr

Font styles to use
Sans Serif

Colors

Designer to choose colors to be used in the design.

Requirements
Must have
• Company Information: Name: TR Périple Rue Paul Dantier KRP Building City: 76420 Bellerive Phone: 0672418053 Email: l.barnier@trperiple.fr
Nice to have
• a card that lives with his time, good agreement with the times
Should not have
• too classic card's lack of a nursery stock, lack of alliance of colors

```html
<!DOCTYPE html>
<html lang="fr">
<head>
<meta charset="utf-8">
<title>TR Périple – cartes de visite</title>
<link rel="stylesheet" href="https://fonts.googleapis.com/css2?family=Jost:wght@400;500;600&display=swap">
<style>
  :root {
    --backdrop: #ececec;
    --green-light: #a6e234;
    --green-mid: #7fd125;
    --green-deep: #3fae16;
    --brand-green: #6cc524;
    --card-white: #ffffff;
    --card-grey: #ececec;
    --ink: #2b2b2b;
    --halftone-grey: rgba(0,0,0,0.09);
    --halftone-green: rgba(40,140,10,0.35);
  }
  * { margin: 0; padding: 0; box-sizing: border-box; }
  html, body { width: 1200px; height: 900px; overflow: hidden; }
  body {
    background: radial-gradient(ellipse at 50% 30%, #ffffff 0%, var(--backdrop) 75%);
    font-family: "Jost", "Futura", sans-serif;
    position: relative;
  }
  .card {
    position: absolute;
    width: 304px;
    height: 200px;
    box-shadow: 0 6px 14px rgba(0,0,0,0.18);
    overflow: hidden;
  }
  .card-front {
    left: 274px; top: 396px;
    background: linear-gradient(135deg, var(--green-light) 0%, var(--green-mid) 55%, var(--green-deep) 100%);
  }
  .card-back {
    left: 656px; top: 458px;
    background: linear-gradient(160deg, var(--card-white) 40%, var(--card-grey) 100%);
  }
  .halftone {
    position: absolute;
    right: 0; bottom: 0;
    width: 60%; height: 100%;
  }
  .card-front .halftone {
    background: radial-gradient(ellipse at 100% 80%, var(--halftone-green) 0%, transparent 65%);
  }
  .card-back .halftone {
    background: radial-gradient(ellipse at 100% 100%, var(--halftone-grey) 0%, transparent 70%);
  }
  .front-name {
    position: absolute;
    left: 66px; top: 36px;
    color: #ffffff;
    font-weight: 600;
    line-height: 1;
  }
  .front-name .initials { display: block; font-size: 100px; letter-spacing: -1px; }
  .front-name .word { display: block; font-size: 28px; letter-spacing: 3px; margin-top: -2px; }
  .back-name {
    position: absolute;
    left: 34px; top: 22px;
    color: var(--brand-green);
    font-weight: 500;
    font-size: 27px;
    letter-spacing: 2px;
  }
  .contact-list {
    position: absolute;
    left: 26px; top: 80px;
    list-style: none;
    color: var(--ink);
    font-size: 14px;
    line-height: 1.15;
  }
  .contact-list li {
    display: flex;
    align-items: flex-start;
    gap: 10px;
    margin-bottom: 9px;
  }
  .contact-list svg { flex: none; width: 17px; height: 17px; fill: var(--brand-green); }
</style>
</head>
<body>
  <section class="card card-front" aria-label="Recto de la carte">
    <div class="halftone" role="img" aria-label="Motif de points en demi-teinte vert"></div>
    <h1 class="front-name"><span class="initials">TR</span><span class="word">PÉRIPLE</span></h1>
  </section>

  <section class="card card-back" aria-label="Verso de la carte">
    <div class="halftone" role="img" aria-label="Motif de points en demi-teinte gris"></div>
    <h2 class="back-name">TR PÉRIPLE</h2>
    <ul class="contact-list">
      <li>
        <svg viewBox="0 0 24 24" aria-hidden="true"><path d="M12 1a8 8 0 0 0-8 8c0 6 8 14 8 14s8-8 8-14a8 8 0 0 0-8-8zm0 11a3 3 0 1 1 0-6 3 3 0 0 1 0 6z"/></svg>
        <span>Rue Paul Dantier, Bâtiment KRP<br>Bellerive 76420</span>
      </li>
      <li>
        <svg viewBox="0 0 24 24" aria-hidden="true"><rect x="2" y="2" width="20" height="20" rx="4"/><path fill="#fff" d="M8 6c1 0 1.5 2 1.5 3s-1 1-1 2 2 4 3 4 1-1 2-1 3 .5 3 1.5-1 2-2 2c-4 0-8.5-4.5-8.5-8.5 0-1 1-3 2-3z"/></svg>
        <span>06 72 41 80 53</span>
      </li>
      <li>
        <svg viewBox="0 0 24 24" aria-hidden="true"><rect x="1" y="5" width="22" height="14" rx="1"/><path d="M2 6l10 7 10-7" stroke="#fff" stroke-width="1.6" fill="none"/></svg>
        <span>l.barnier@trperiple.fr</span>
      </li>
    </ul>
  </section>
</body>
</html>
```